Vantrel Card

We want a business card that shows people who we are the log attached was designed by the designers on craft hive,we are using the OO in the logo (speech bubbles as our icon,so please make that part of the card ) keep the colouring the same as the logo design and we will be using high end production on the card using silver foil as the icon to make it stand out.
As Vantrel we specialise in finding influencers through social networks for brands, so if you used flimbo to comment about sports products and you were followed by of lot of users and interacted with those users then the algorithm finds you and we contact you to work for our clients as a company we then have a set of influencers that we use to support new sports products.
Also we use our algorithm to help athletes,models etc to be scored via there digital influence so when say Vorta KX ask me to find a skater that is not so much a podium rider but is more digital focused for a digital campaign then we work out who those guys or girls are to help Vorta KX
Vantrel is the name of the product and company, However I just wanted to give you the rationale of why we chose vantrel in the first place. Marbo itself is an 'abbreviation' from the proper name Alsander Wick from Tale of the Iron Hills. The character was able to look into the eskavor (sometimes translated as "Seeing Stone" but literally meaning "Farsighted" or "One that Sees from Afar") and see into the far corners of the Universe. Much in the same way as the platform has been developed is able to look into the far corners of the social network arena to help brands and Athletes will be able to see how they rated....but don't worry i don't go running around in the woods with a foam Axe and an army of dwarfs!!!
Digital Directors,Brand Directors,Athletes,Models,Celebrities and agents
Business

```html
<!DOCTYPE html>
<html lang="en">
<head>
<meta charset="utf-8">
<title>Vantrel Business Card</title>
<link rel="stylesheet" href="https://fonts.googleapis.com/css2?family=Questrial&display=swap">
<style>
  :root {
    --page: #f4f4f4;
    --card-light: #ffffff;
    --card-light-shade: #ececec;
    --card-dark: #2a2c2e;
    --card-dark-deep: #1f2022;
    --brand-blue: #4bb8ea;
    --ink: #2b2b2b;
    --ink-soft: #7a7a7a;
    --on-dark: #f2f2f2;
    --silver: #c9cacc;
  }
  * { box-sizing: border-box; margin: 0; padding: 0; }
  html, body { width: 1200px; height: 900px; overflow: hidden; }
  body {
    background: var(--page);
    font-family: "Questrial", "Century Gothic", sans-serif;
    position: relative;
  }
  .card {
    position: absolute;
    top: 300px;
    width: 520px;
    height: 300px;
    border-radius: 20px;
    overflow: hidden;
    box-shadow: 0 14px 30px rgba(0,0,0,0.18);
  }
  .card-front { left: 50px; background: var(--card-dark); }
  .card-back {
    left: 630px;
    background: linear-gradient(160deg, var(--card-dark) 0%, var(--card-dark-deep) 100%);
    display: flex;
    align-items: center;
    justify-content: center;
  }
  .front-top {
    position: absolute; left: 0; top: 0; width: 100%; height: 150px;
    background: linear-gradient(180deg, var(--card-light-shade) 0%, var(--card-light) 60%);
  }
  .front-stripe {
    position: absolute; left: 0; top: 150px; width: 100%; height: 9px;
    background: var(--brand-blue);
  }
  .brand-name {
    position: absolute; left: 24px; top: 58px;
    font-size: 66px; line-height: 1; color: var(--brand-blue);
    letter-spacing: -1px;
  }
  .holder { position: absolute; right: 34px; top: 30px; text-align: right; }
  .holder-name { font-size: 21px; color: var(--ink); }
  .holder-role { font-size: 17px; color: var(--ink-soft); margin-top: 2px; }
  .contact-list {
    position: absolute; left: 28px; top: 192px; list-style: none;
    color: var(--on-dark); font-size: 16px; line-height: 22px;
  }
  .contact-list li { display: flex; align-items: center; gap: 6px; }
  .contact-icon { width: 16px; height: 16px; flex: none; }
  .social {
    position: absolute; right: 34px; bottom: 40px;
    color: var(--on-dark); font-size: 15px;
    display: flex; align-items: center; gap: 8px;
  }
  .social-name { color: var(--brand-blue); }
  .back-mark {
    font-size: 96px; color: var(--silver); letter-spacing: -1px; line-height: 1;
  }
</style>
</head>
<body>
  <section class="card card-front" aria-label="Card front">
    <div class="front-top"></div>
    <div class="front-stripe"></div>
    <div class="brand-name">vantrel</div>
    <div class="holder">
      <div class="holder-name">Dorian Hale</div>
      <div class="holder-role">Manager</div>
    </div>
    <ul class="contact-list">
      <li>
        <svg class="contact-icon" viewBox="0 0 16 16" aria-hidden="true"><path d="M3 1.5l3 3-1.6 1.8c.9 2 2.4 3.5 4.3 4.4L10.5 9l3 3-2 2.3C6.2 13.6 2.4 9.8 1.2 3.6z" fill="#4bb8ea"/></svg>
        <span>1800 555 014</span>
      </li>
      <li>
        <svg class="contact-icon" viewBox="0 0 16 16" aria-hidden="true"><g fill="none" stroke="#4bb8ea" stroke-width="1.4"><circle cx="8" cy="8" r="6.3"/><ellipse cx="8" cy="8" rx="2.8" ry="6.3"/><path d="M1.7 8h12.6M2.8 4.6h10.4M2.8 11.4h10.4"/></g></svg>
        <span>www.vantrel.com</span>
      </li>
      <li>
        <svg class="contact-icon" viewBox="0 0 16 16" aria-hidden="true"><rect x="1.5" y="3.5" width="13" height="9" rx="1" fill="#4bb8ea"/><path d="M2 4.2l6 4.6 6-4.6" fill="none" stroke="#2a2c2e" stroke-width="1.3"/></svg>
        <span>info@vantrel.com</span>
      </li>
      <li>
        <svg class="contact-icon" viewBox="0 0 16 16" aria-hidden="true"><path d="M8 1.5L1 8h2v6.5h3.8v-4h2.4v4H13V8h2z" fill="#4bb8ea"/></svg>
        <span>PO Box 7721 Harbour Centre</span>
      </li>
    </ul>
    <div class="social">
      <span>Like us on</span>
      <span class="social-name">Chatterly</span>
      <span class="social-name">flimbo</span>
    </div>
  </section>

  <section class="card card-back" aria-label="Card back">
    <div class="back-mark">vantrel</div>
  </section>
</body>
</html>
```